■依頼の目的/概要
ピッツェリア(ナポリピッツァ専門店)の店頭に並ぶ商品用のPOPのデザインをお願いします。

■依頼詳細
ピッツェリア(ナポリピッツァ専門店)に並ぶ商品1点のデザインをお願いします。
夏物商品の紹介なので、締め切りが早くて恐縮です。
欲しい内容は
「4色スムージー」
「4色の内訳は、グリーン、パープル、イエロー、ブラック」
それぞれの原料と効能は
「グリーン
・野菜たっぷり&おなかの調子を整える!
・アボカド、小松菜、セロリ、その他」
「パープル
・ポリフェノール&プロアントシアニンで、ダイエット効果!血行促進!コラーゲン生成促進。
・4種のベリー(ブルーベリー、ラズベリー、クランベリー、ストロベリー)、豆乳、その他」
「イエロー
・美肌サポート!&アンチエイジング!
・マンゴー、チアシード(スーパーフード)、ココナツウォーター、その他」
「ブラック
・ビタミン豊富&整腸作用!DHA!低GI!
・ゴマ、豆乳、アガベシロップ(スーパーフード)、その他」
「各500円」価格は税込みですが、特にその表記は必要ないです。
「上手に効能をPRする」
「ランチタイムは、ピザをたのんだお客様には100円引き(400円)で提供します」
商品画像(添付の物ですが、ほかに”こういう構図のものが欲しい”など指定があれば、撮影し直すことも可能)
文言については、改変まったくokです。むしろ、素敵な表現を考えていただけるとありがたいです。原材料はそれぞれその他、と書いてあるように、具体的に書いてある物以外にも使用しています。
A4片面で印刷、ラミネート処理して店内に置いたり掲示したりする予定です。

■重視する点
オシャレであること。美味しそうであること。
ターゲットは30台~40台の女性。
photoshopデータで納品だとありがたいです。PDFやjpgでもok。

その他何かご不明な点がございましたら、お気軽にご質問下さい。
よろしくお願いいたします。
背景の白い商品画像を追加しました。
画質向上のため、写真を差し替えました。
たくさんのご提案をいただき、誠にありがとうございました。
7/13に社内選考を行う予定です。しばらくお待ち下さい。

大変魅力的なご提案が多かったため、選考には大変苦慮しましたが、
・女性からの支持が多かった点
・こちらの要望をしっかりくみ取っていただけた点
・全体的な華やかさ
等から、今回は当選を決めさせていただきました。
とても素敵なプランを採用でき、大変満足しております。

このたびは、大変魅力的なご提案を数多くいただき、ありがとうございました。正直大変目移りしてしまい、最終的に決まるまで二転三転したりしました。今回当選とさせていただかなかった方とも、またどこかでお仕事を依頼申し上げられたら幸いです。今後ともよろしくお願い申し上げます。

```html
<!DOCTYPE html>
<html lang="ja">
<head>
<meta charset="utf-8">
<title>Luna Forno Summer Drink - ヘルシー4色スムージー</title>
<link rel="stylesheet" href="https://fonts.googleapis.com/css2?family=M+PLUS+Rounded+1c:wght@500;700;800&family=Playfair+Display:wght@500&display=swap">
<style>
:root{
  --header:#3eb6c9;
  --badge:#8fd3de;
  --white:#ffffff;
  --ink:#2b2b2b;
  --accent:#e0245a;
  --purple:#8e2f6f;
  --yellow:#e2a400;
  --black:#4a3d38;
  --green:#6f9a1f;
  --line-purple:#b24c86;
  --line-yellow:#e8b33a;
  --line-black:#7a6a62;
  --line-green:#8db43e;
  --tint-purple:#f6dbe8;
  --tint-yellow:#fdf0c8;
  --tint-black:#ecdfe6;
  --tint-green:#e4f0cf;
}
*{margin:0;padding:0;box-sizing:border-box}
html,body{width:847px;height:1200px;overflow:hidden;background:var(--white)}
body{font-family:"M PLUS Rounded 1c",sans-serif;color:var(--ink)}
.poster{position:relative;width:847px;height:1200px;overflow:hidden;
  background:
    radial-gradient(ellipse 260px 200px at 300px 440px,var(--tint-purple),transparent 70%),
    radial-gradient(ellipse 260px 200px at 700px 450px,var(--tint-yellow),transparent 70%),
    radial-gradient(ellipse 260px 200px at 250px 900px,var(--tint-black),transparent 70%),
    radial-gradient(ellipse 260px 200px at 700px 900px,var(--tint-green),transparent 70%),
    var(--white);}
.header{position:absolute;left:0;top:0;width:847px;height:100px;background:var(--header)}
.header__kicker{position:absolute;left:40px;top:10px;color:var(--white);font-weight:800;font-size:24px;letter-spacing:.5px}
.header__title{position:absolute;left:40px;top:42px;color:var(--white);font-weight:800;font-size:44px;letter-spacing:2px}
.price-badge{position:absolute;right:0;top:0;width:200px;height:110px}
.price-badge svg{position:absolute;inset:0}
.price-badge__text{position:absolute;right:22px;top:16px;text-align:right;color:var(--white);font-weight:800;line-height:1.05}
.price-badge__all{font-size:28px;display:block}
.price-badge__yen{font-size:36px;display:block}
.price-badge__yen small{font-size:22px}

.flavor__label{position:absolute;font-family:"Playfair Display",serif;font-size:38px;font-weight:500;line-height:1.2}
.flavor__photo{position:absolute;width:330px;height:330px;border-radius:14px}
.flavor__caption{position:absolute;font-size:16px;font-weight:700;line-height:1.45}
.flavor__caption b{font-size:19px}

.bubble{position:absolute;background:var(--white);border:3px solid;border-radius:12px;padding:12px 10px;
  text-align:center;color:var(--accent);font-weight:800;font-size:19px;line-height:1.38;white-space:nowrap}
.bubble::after{content:"";position:absolute;left:42px;bottom:-13px;width:22px;height:22px;background:var(--white);
  border-right:3px solid;border-bottom:3px solid;border-color:inherit;transform:rotate(45deg) skew(8deg,8deg)}
.bubble--purple{border-color:var(--line-purple)}
.bubble--yellow{border-color:var(--line-yellow)}
.bubble--black{border-color:var(--line-black)}
.bubble--green{border-color:var(--line-green)}

.lunch{position:absolute;left:0;bottom:0;width:847px;height:58px;display:flex;align-items:center;justify-content:center;
  font-size:21px;font-weight:800;border-top:3px solid var(--header)}
</style>
</head>
<body>
<div class="poster">
  <header class="header">
    <div class="header__kicker">Luna Forno Summer Drink!!</div>
    <h1 class="header__title">ヘルシー４色スムージー</h1>
    <div class="price-badge">
      <svg width="200" height="110" viewBox="0 0 200 110"><path d="M20 0 H200 V110 C150 120 120 95 95 80 C60 95 25 80 30 50 C5 40 5 15 20 0Z" fill="var(--badge)"/></svg>
      <div class="price-badge__text"><span class="price-badge__all">ALL</span><span class="price-badge__yen">500 <small>yen</small></span></div>
    </div>
  </header>

  <!-- Purple -->
  <div class="flavor__label" style="left:50px;top:170px;color:var(--purple)">Purple</div>
  <div class="flavor__photo" role="img" aria-label="パープルスムージーのグラス写真" style="left:45px;top:225px;background:linear-gradient(180deg,#f7e8ee,#b0336f 45%,#7a1f4e)"></div>
  <div class="bubble bubble--purple" style="left:215px;top:150px;width:230px">ポリフェノール＆<br>プロアントシアニンで<br>ダイエット効果！<br>血行促進！<br>コラーゲン生成促進！</div>
  <div class="flavor__caption" style="left:45px;top:563px;width:380px"><b>◆ パープル</b><br>（ブルーベリー、ラズベリー、クランベリー、<br>ストロベリー、豆乳、その他）</div>

  <!-- Yellow -->
  <div class="flavor__label" style="left:540px;top:170px;color:var(--yellow)">Yellow</div>
  <div class="flavor__photo" role="img" aria-label="イエロースムージーのグラス写真" style="left:450px;top:225px;background:linear-gradient(180deg,#fdf3d6,#f6b21c 45%,#e08a00)"></div>
  <div class="bubble bubble--yellow" style="left:630px;top:232px;width:200px">美肌サポート！<br>＆<br>アンチエイジング！</div>
  <div class="flavor__caption" style="left:450px;top:563px;width:390px"><b>◆ イエロー</b><br>（マンゴー、チアシード（スーパーフード）、<br>ココナツウォーター、その他）</div>

  <!-- Black -->
  <div class="flavor__label" style="left:50px;top:646px;color:var(--black)">Black</div>
  <div class="flavor__photo" role="img" aria-label="ブラックスムージーのグラス写真" style="left:45px;top:700px;background:linear-gradient(180deg,#f2ebe8,#8b7a70 45%,#5a4a42)"></div>
  <div class="bubble bubble--black" style="left:240px;top:680px;width:180px">ビタミン豊富<br>＆<br>整腸作用！<br>DHA！<br>低GI！</div>
  <div class="flavor__caption" style="left:45px;top:1040px;width:390px"><b>◆ ブラック</b><br>（ゴマ、豆乳、<br>アガベシロップ（スーパーフード）、その他）</div>

  <!-- Green -->
  <div class="flavor__label" style="left:540px;top:646px;color:var(--green)">Green</div>
  <div class="flavor__photo" role="img" aria-label="グリーンスムージーのグラス写真" style="left:450px;top:700px;background:linear-gradient(180deg,#eef5e0,#8fb33a 45%,#5f8a1a)"></div>
  <div class="bubble bubble--green" style="left:640px;top:712px;width:190px">野菜たっぷり<br>＆<br>おなかの調子を<br>整える！</div>
  <div class="flavor__caption" style="left:450px;top:1040px;width:390px"><b>◆ グリーン</b><br>（アボカド、小松菜、セロリ、その他）</div>

  <footer class="lunch">● ランチタイム … ピザをご注文のお客様にはスムージー100円引！</footer>
</div>
</body>
</html>
```